Technical Communications firm needs an article turned into a white paper

We want to redesign a 3-part blog series into a white paper that we can print for a conference. I've consolidated the three posts into the attached Word document.

We are looking for a light, easy to read design. Good use of graphics to support the message. I've added the graphics we used in the original post.

You can view them at
http://www.quillmarrowgroup.com/blog/are-you-satisfied-with-your-dita-solution/

Target Market(s)

Product managers from High-tech, Finance, and Medical industries.

Industry/Entity Type

Information Technology

Colors

Designer to choose colors to be used in the design.

Requirements
Must have
• Must be modern, light, easy to read and slick design. Try to incorporate the graphics provided, but feel free to add more. Must retain the lists and tables.
• Must align with our website/brand.
• Must be easy to read. So not too busy.
• Please move all footnotes to endnotes. You'll need to rework the numbering.
Nice to have
• Awesome coverpage.
Should not have
• Hokey clipart. Not too heavy or hard to read.

```html
<!DOCTYPE html>
<html lang="en">
<head>
<meta charset="utf-8">
<title>Part 1: Skills Development — White Paper Spread</title>
<link href="https://fonts.googleapis.com/css2?family=Ubuntu:ital,wght@0,400;0,500;0,700;1,400&family=Open+Sans:ital,wght@0,400;0,600;1,400&display=swap" rel="stylesheet">
<style>
  :root{
    --backdrop:#dcdcd8;
    --paper:#ffffff;
    --ink:#474a4f;
    --ink-soft:#8a8d92;
    --heading-blue:#2b4fa0;
    --navy:#2a4a8c;
    --sky:#5aa3d7;
    --rule:#d4d8de;
    --photo-top:#4f8a67;
    --photo-bottom:#2f5e45;
    --disc-1:#bcdcf0;
    --disc-2:#82c0da;
    --disc-3:#4d92c8;
    --disc-4:#2e6894;
  }
  *{box-sizing:border-box;margin:0;padding:0}
  html,body{width:1200px;height:804px;overflow:hidden}
  body{background:var(--backdrop);font-family:"Open Sans",Arial,sans-serif;color:var(--ink);position:relative}
  .page{position:absolute;top:14px;width:578px;height:776px;background:var(--paper);overflow:hidden}
  .page--left{left:20px;box-shadow:inset -14px 0 18px -14px rgba(0,0,0,.18)}
  .page--right{left:602px;box-shadow:inset 14px 0 18px -14px rgba(0,0,0,.18)}

  /* left page */
  .hero-photo{height:292px;background:linear-gradient(160deg,var(--photo-top),var(--photo-bottom))}
  .article-head{padding:24px 44px 0 44px}
  .article-title{font-family:"Ubuntu",sans-serif;font-weight:500;font-size:25px;color:#3d4046}
  .byline{font-family:"Ubuntu",sans-serif;font-style:italic;font-size:12px;text-align:right;margin-top:6px;color:#3d4046}
  .byline-role{font-family:"Ubuntu",sans-serif;font-style:italic;font-size:9.5px;text-align:right;margin-top:12px;color:var(--ink)}
  .body-text{font-size:9.4px;line-height:1.42;color:var(--ink)}
  .intro{margin:22px 44px 0 44px}
  .section-heading{font-family:"Ubuntu",sans-serif;font-weight:500;color:var(--heading-blue);font-size:18px}
  .left-heading{margin:20px 44px 0 44px}
  .left-lead{margin:8px 44px 0 44px}
  .rank-chart{position:absolute;left:40px;top:548px}
  .rank-label{font-size:9.4px;fill:var(--ink);font-family:"Open Sans",sans-serif}

  .folio{position:absolute;bottom:20px;font-size:8px;color:var(--ink-soft)}
  .folio strong{font-family:"Ubuntu",sans-serif;font-weight:500;color:var(--sky);font-size:10px;letter-spacing:.5px}
  .contact{position:absolute;font-size:7.2px;color:var(--ink-soft)}

  /* right page */
  .series-tab{position:absolute;top:0;right:0;height:22px;width:230px;background:var(--sky);color:#fff;
    font-size:8.4px;display:flex;align-items:center;justify-content:flex-end;gap:6px;padding-right:12px;
    clip-path:polygon(0 0,100% 0,100% 100%,14px 100%)}
  .series-tab .dot{width:10px;height:10px;border-radius:50%;background:#fff}
  .site-url{position:absolute;top:26px;left:40px;font-size:8px;letter-spacing:1.6px;color:var(--ink-soft)}
  .right-body{position:absolute;top:52px;left:40px;right:34px}
  .right-body p + p{margin-top:9px}
  .right-body .section-heading{margin:14px 0 6px}
  .compare-table{width:100%;border-collapse:collapse;margin-top:12px;font-size:8.8px;line-height:1.3}
  .compare-table th{font-family:"Ubuntu",sans-serif;font-weight:500;font-size:12px;color:#fff;padding:6px 0;text-align:center}
  .compare-table th.writing{background:var(--navy)}
  .compare-table th.markup{background:var(--sky)}
  .compare-table td{border:1px solid var(--rule);padding:6px 7px;vertical-align:middle;height:38px}
  .compare-table td.tick{width:26px;text-align:center;font-size:11px;color:var(--ink)}
  .table-caption{font-size:7.4px;font-style:italic;color:var(--ink-soft);text-align:right;margin-top:4px}
  .checklist{list-style:none;margin-top:8px}
  .checklist li{display:flex;gap:8px;align-items:flex-start;font-size:9.2px;line-height:1.4;margin-bottom:7px}
  .checklist svg{flex:none;margin-top:1px}
</style>
</head>
<body>

<section class="page page--left">
  <div class="hero-photo" role="img" aria-label="Photo of a puzzled man looking up at a green chalkboard with the hand-written question what am I supposed to do"></div>

  <header class="article-head">
    <h1 class="article-title">Part 1: Skills Development</h1>
    <p class="byline">By Dana Whitlock</p>
    <p class="byline-role">President of Quill Marrow Group Inc.</p>
  </header>

  <p class="body-text intro">This article is part of a series based on the results of a survey of more than 250 technical communication professionals conducted by The Docs Drover in 2017 entitled The DITA Satisfaction Survey[i]. In the survey, almost two-thirds of respondents voiced concerns with their DITA deployment. In our previous article, we introduced the overall results from the survey that pertain to users' dissatisfaction with their DITA solution. In this article, we examine the top rated issues pertaining to skills development.</p>

  <h2 class="section-heading left-heading">Issues related to skills development</h2>
  <p class="body-text left-lead">The top-ranked reported issues fall under the category of skill development and training. These include</p>

  <svg class="rank-chart" width="500" height="180" viewBox="0 0 500 180" aria-label="Stacked ranking of top skills issues">
    <ellipse cx="82" cy="136" rx="74" ry="30" fill="var(--disc-4)"/>
    <ellipse cx="80" cy="104" rx="74" ry="30" fill="var(--disc-3)"/>
    <ellipse cx="78" cy="72" rx="74" ry="30" fill="var(--disc-2)"/>
    <ellipse cx="76" cy="40" rx="74" ry="30" fill="var(--disc-1)"/>
    <g stroke="#9aa0a6" stroke-width=".8" fill="#fff">
      <line x1="150" y1="38" x2="292" y2="32"/><circle cx="294" cy="32" r="2.6"/>
      <line x1="152" y1="70" x2="296" y2="66"/><circle cx="298" cy="66" r="2.6"/>
      <line x1="154" y1="102" x2="300" y2="98"/><circle cx="302" cy="98" r="2.6"/>
      <line x1="156" y1="134" x2="304" y2="130"/><circle cx="306" cy="130" r="2.6"/>
    </g>
    <text class="rank-label" x="312" y="26">How do I reuse content? Ranked 1st by</text>
    <text class="rank-label" x="312" y="38">75% of respondents</text>
    <text class="rank-label" x="316" y="60">How do I make DITA do what I want it to</text>
    <text class="rank-label" x="316" y="72">do? Ranked 2nd by 69% of respondents</text>
    <text class="rank-label" x="320" y="92">Where can I get DITA training? Ranked</text>
    <text class="rank-label" x="320" y="104">3rd by 64% of respondents, and</text>
    <text class="rank-label" x="324" y="124">How do I create DITA content? Ranked</text>
    <text class="rank-label" x="324" y="136">8th by 56% of respondents.</text>
  </svg>

  <p class="contact" style="right:40px;bottom:44px">more-info@quillmarrowgroup.com &nbsp;|&nbsp; +1 (555) 014-2290, Press 1</p>
  <p class="folio" style="left:40px"><strong>PAGE 10</strong> | Quill Marrow Group Inc.</p>
</section>

<section class="page page--right">
  <div class="series-tab">Are you satisfied with your DITA solution? <span class="dot"></span></div>
  <p class="site-url">www.quillmarrowgroup.com</p>

  <div class="right-body">
    <p class="body-text">This problem area is far and away the most pressing obstacle for a successful DITA deployment. Too often authors are left to figure out how to adapt to writing for DITA on their own. Organizations will normally invest in tools training—and may even opt for a short training course to learn about DITA—but they rarely make the effort to train writers how to author modular, structured topics of content designed for reuse. It is easy to overlook this training aspect and assume that writers will naturally adapt to this new way of writing. But, those assumptions can lead to big problems.</p>
    <p class="body-text">In a poll conducted in a recent webinar[ii] where half of the participants indicated they were already using DITA, a full 70% indicated that they had no formal DITA training. Of those participants, nearly 60% were self-taught while the others had no training at all. It's no wonder that dissatisfaction is the norm.</p>

    <h2 class="section-heading">Selecting the best training for your needs</h2>
    <p class="body-text">There are many training options available to learn about DITA. Selecting the best training for your team entails examining what it is you need to learn. Most DITA training courses cover the features and walk you through the structures and mechanics of the standard. These courses demonstrate how to markup content, but will often not teach you how to rethink and restructure your content to take advantage of DITA's features. Consider the differences between structured writing and structured markup.</p>

    <table class="compare-table">
      <thead>
        <tr><th class="writing" colspan="2">Structured Writing</th><th class="markup" colspan="2">Structured Markup</th></tr>
      </thead>
      <tbody>
        <tr><td class="tick">√</td><td>Coined by Martin Ellery in the 1960's as a means of analyzing, organizing, and presenting information for optimal human consumption</td><td class="tick">√</td><td>Allows authors to markup words, phrases, and sections of content for presentation and for meaning for consumption by machines</td></tr>
        <tr><td class="tick">√</td><td>Promotes patterns for format and syntax that become easily recognizable and predictable</td><td class="tick">√</td><td>Is validated using standard sets of rules that specify consistent and predictable patterns</td></tr>
        <tr><td class="tick">√</td><td>Relies on consistently labelling and chunking information into easily scannable text</td><td class="tick">√</td><td>Specifies what content goes where but does not limit or restrict how the content is written</td></tr>
        <tr><td class="tick">√</td><td>Introduces universal information typing based on intended reader response</td><td class="tick">√</td><td>Provides a rich underlying metadata layer for capturing properties related to the content</td></tr>
      </tbody>
    </table>
    <p class="table-caption">Table reproduced from "Building Team Momentum at the Head of the Structured Content Line[iii]".</p>

    <h2 class="section-heading">Continuous collaborative learning</h2>
    <p class="body-text">Organizations that wisely invest in comprehensive training for their writing teams also recognize the importance of continuous learning and recurring training. To stay on top of knowledge sharing in your team, consider the following collaboration activities:</p>

    <ul class="checklist body-text">
      <li><svg width="10" height="10" viewBox="0 0 10 10"><rect x=".5" y=".5" width="9" height="9" fill="none" stroke="#555"/><path d="M2 5l2 2 4-5" fill="none" stroke="#333" stroke-width="1.3"/></svg>Schedule regular checkpoints where your team discusses what they've learned with other members of the team.</li>
      <li><svg width="10" height="10" viewBox="0 0 10 10"><rect x=".5" y=".5" width="9" height="9" fill="none" stroke="#555"/><path d="M2 5l2 2 4-5" fill="none" stroke="#333" stroke-width="1.3"/></svg>Assign different members of your team to research and present best practices at regularly scheduled lunch-and-learn sessions.</li>
      <li><svg width="10" height="10" viewBox="0 0 10 10"><rect x=".5" y=".5" width="9" height="9" fill="none" stroke="#555"/><path d="M2 5l2 2 4-5" fill="none" stroke="#333" stroke-width="1.3"/></svg>Attend webinars and seminars on best practices as a group and then debrief together to discuss aspects that should be incorporated into your day-to-day work.</li>
      <li><svg width="10" height="10" viewBox="0 0 10 10"><rect x=".5" y=".5" width="9" height="9" fill="none" stroke="#555"/><path d="M2 5l2 2 4-5" fill="none" stroke="#333" stroke-width="1.3"/></svg>Review and update your content standards regularly as a team to keep your procedures and guidelines current and relevant.</li>
      <li><svg width="10" height="10" viewBox="0 0 10 10"><rect x=".5" y=".5" width="9" height="9" fill="none" stroke="#555"/><path d="M2 5l2 2 4-5" fill="none" stroke="#333" stroke-width="1.3"/></svg>Pair up senior members of your team with new or junior members for regular mentoring and coaching.</li>
    </ul>
  </div>

  <p class="contact" style="left:40px;bottom:22px">more-info@quillmarrowgroup.com &nbsp;|&nbsp; +1 (555) 014-2290, Press 1</p>
  <p class="folio" style="right:34px">Quill Marrow Group Inc. | <strong>PAGE 11</strong></p>
</section>

</body>
</html>
```